AI Layout work for Business Cards, Letterhead and Compliment Slip for Award-winning UK Property Deve

No actual logo or corporate identity design work needed here but some skill required to create layouts for business card, letterhead and compliment slip for this award-winning company.
I can provide AI files featuring the company logo and an initial layout of the business card, (6 versions featuring the same design but for different personnel), along with some initial instructions (with possibly more to follow from the client). The finished layouts for each item need to be print-ready in AI format - 8 in all (6 for each business card plus 1 for letterhead and 1 for compliment slip).
I've given this project a 5-day duration but there may be some flexibility built into that depending on client feedback. Hopefully that won't be a problem.
UPDATE:
The client has been very prescriptive about the layout and design of these. To that end, please find 3 additional pdfs that explain what's required.
1.
All BUSINESS CARDS need to be laid out as per the attached AI file (but see latest pdf to check which layout - there are 2 in the original AI file). Use the details in the RUNE-contact-details.pdf to create 6 individual AI files, one for each card.
2.
Create 2 additional AI files, one each for the LETTERHEAD and the COMPLIMENT SLIP based on the latest mock-up that I've provided (letterhead-layout-final.pdf)
In all, I need EIGHT individual AI files, 6 for each business card, 1 for the letterhead and 1 for the compliment slip. I'd like to get this done as soon as possible now please.
Target Market(s)
Purchasers of upmarket luxury properties - see here: http://www.runeestates.co.uk
Industry/Entity Type
Business
Requirements
Must have
- Layouts need to be cool, understated and uncluttered.
Nice to have
- Please keep it simple! The actual logo background colour is likely to change (awaiting confirmation from client) but accompanying text detail and font (Deja Vu Sans Condensed) can remain as seen in the files below - for the time being at least! That having been said, I'm open to suggestions.
Should not have
- Nothing extreme or ostentatious please.

```html
<!DOCTYPE html>
<html lang="en">
<head>
<meta charset="utf-8">
<title>RUNE Estates Stationery Design Proposal</title>
<link href="https://fonts.googleapis.com/css2?family=Roboto+Condensed:wght@400;700&display=swap" rel="stylesheet">
<style>
:root{
  --page:#ffffff;
  --slate:#5a6478;
  --ink:#3b4560;
  --faint:#e4e5ea;
  --heading:#555555;
  --caption:#444444;
  --shadow:rgba(0,0,0,.35);
}
*{margin:0;padding:0;box-sizing:border-box}
html,body{width:1200px;height:900px;overflow:hidden;background:var(--page)}
body{position:relative;font-family:"Roboto Condensed",Arial,sans-serif;color:var(--ink)}
.proposal-title{position:absolute;left:20px;top:23px;font-size:15px;font-weight:700;color:var(--heading);letter-spacing:.2px}
.sheet{position:absolute;background:#fff;box-shadow:4px 5px 7px var(--shadow);overflow:hidden}
.caption{position:absolute;font-size:7.5px;font-weight:700;color:var(--caption);white-space:nowrap}
.footer-bar{position:absolute;left:0;right:0;bottom:0;background:var(--slate);color:#fff;font-weight:700;display:flex;align-items:center;white-space:nowrap}
.brand{display:flex;align-items:center;gap:4px;color:var(--slate);font-weight:700;position:absolute;white-space:nowrap}
.brand-square{background:var(--slate);display:block}
.address{position:absolute;font-size:5px;line-height:6.3px;color:var(--ink);white-space:nowrap}
.address .company{font-weight:700}
.address .gap{height:6px}
.faint-disc{position:absolute;border-radius:50%;background:var(--faint)}
.photo{position:absolute;inset:0}
.tagline{position:absolute;color:#fff;white-space:nowrap}

/* Letterhead */
.letterhead{left:34px;top:157px;width:322px;height:457px}
.letterhead .brand{left:234px;top:18px;font-size:14px}
.letterhead .brand-square{width:14px;height:14px}
.letterhead .address{left:234px;top:66px}
.letterhead .faint-disc{left:16px;top:142px;width:290px;height:290px}
.letterhead .footer-bar{height:16px;font-size:7px;padding-left:14px}
.letterhead-back{left:383px;top:233px;width:323px;height:455px}
.letterhead-back .photo{background:linear-gradient(180deg,#4b4f5f 0%,#5d6271 45%,#6f7078 75%,#565a66 100%)}
.letterhead-back .faint-disc{left:70px;top:150px;width:250px;height:250px;background:rgba(255,255,255,.18)}
.letterhead-back .tagline{left:87px;top:265px;font-size:11.5px}

/* Compliment slip */
.slip{left:749px;top:144px;width:323px;height:152px}
.slip .faint-disc{left:6px;top:12px;width:118px;height:118px}
.slip .greeting{position:absolute;left:17px;top:66px;font-size:7px;font-weight:700;color:var(--ink);white-space:nowrap}
.slip .brand{left:234px;top:20px;font-size:13px}
.slip .brand-square{width:13px;height:13px}
.slip .address{left:234px;top:65px;font-size:4.6px;line-height:5.9px}
.slip .footer-bar{height:16px;font-size:7px;padding-left:14px}
.slip-back{left:843px;top:318px;width:322px;height:152px}
.slip-back .photo{background:linear-gradient(90deg,#8b8690 0%,#a59b98 30%,#8c8893 60%,#7d7f8f 100%)}
.slip-back .faint-disc{left:12px;top:20px;width:118px;height:118px;background:rgba(255,255,255,.2)}
.slip-back .tagline{left:79px;top:56px;font-size:11px}

/* Business card */
.card{left:753px;top:558px;width:130px;height:87px}
.card .address{left:6px;top:6px;font-size:3.8px;line-height:4.8px}
.card .brand{left:76px;top:12px;font-size:10px}
.card .brand-square{width:9px;height:9px}
.card .footer-bar{height:13px;font-size:5px;padding-left:6px}
.card-back{left:895px;top:607px;width:130px;height:85px}
.card-back .photo{background:linear-gradient(135deg,#8a8c97 0%,#6c7182 50%,#596176 100%)}
.card-back .person{position:absolute;left:7px;top:27px;color:#fff;font-size:7.5px;font-weight:700;white-space:nowrap}
.card-back .contact{position:absolute;left:7px;top:44px;color:#fff;font-size:6.5px;line-height:9px;white-space:nowrap}
.card-back .contact b{font-weight:700}
.card-back .rule{position:absolute;left:7px;right:7px;top:69px;height:1px;background:rgba(255,255,255,.7)}
.card-back .tagline{left:7px;top:73px;font-size:5px;font-weight:700}
</style>
</head>
<body>
<h1 class="proposal-title">RUNE ESTATES STATIONERY DESIGN PROPOSAL</h1>

<section class="sheet letterhead">
  <div class="faint-disc"></div>
  <div class="brand"><span class="brand-square"></span>RUNE</div>
  <div class="address">
    <div class="company">RUNE Exclusive Estates</div>
    <div>Orchard Barn House</div>
    <div>Orchard Barn Lane</div>
    <div>Little Hadley</div>
    <div>Berkshire</div>
    <div>RG9 2XY</div>
    <div class="gap"></div>
    <div><b>T.</b> +44 (0)1632 960 418</div>
    <div><b>E.</b> enquiries@runeestates.co.uk</div>
  </div>
  <div class="footer-bar">www.runeestates.co.uk</div>
</section>
<p class="caption" style="left:34px;top:622px">Double Sided A4 Letterhead</p>

<section class="sheet letterhead-back">
  <div class="photo" role="img" aria-label="Photograph of a restored brick townhouse lit at dusk"></div>
  <div class="faint-disc"></div>
  <p class="tagline">Giving lasting character to period homes</p>
</section>

<section class="sheet slip">
  <div class="faint-disc"></div>
  <p class="greeting">WITH COMPLIMENTS</p>
  <div class="brand"><span class="brand-square"></span>RUNE</div>
  <div class="address">
    <div class="company">RUNE Exclusive Estates</div>
    <div>Orchard Barn House</div>
    <div>Orchard Barn Lane</div>
    <div>Little Hadley</div>
    <div>Berkshire</div>
    <div>RG9 2XY</div>
    <div class="gap"></div>
    <div><b>T.</b> +44 (0)1632 960 418</div>
    <div><b>E.</b> enquiries@runeestates.co.uk</div>
  </div>
  <div class="footer-bar">www.runeestates.co.uk</div>
</section>

<section class="sheet slip-back">
  <div class="photo" role="img" aria-label="Photograph of a classic hallway staircase with ornate banister"></div>
  <div class="faint-disc"></div>
  <p class="tagline">Giving lasting character to period homes</p>
</section>
<p class="caption" style="left:843px;top:477px">Double Sided DL Compliment Slip</p>

<section class="sheet card">
  <div class="address">
    <div class="company">RUNE Exclusive Estates</div>
    <div>Orchard Barn House</div>
    <div>Orchard Barn Lane</div>
    <div>Little Hadley</div>
    <div>Berkshire</div>
    <div>RG9 2XY</div>
    <div class="gap"></div>
    <div><b>T.</b> +44 (0)1632 960 418</div>
    <div><b>E.</b> enquiries@runeestates.co.uk</div>
  </div>
  <div class="brand"><span class="brand-square"></span>RUNE</div>
  <div class="footer-bar">www.runeestates.co.uk</div>
</section>
<p class="caption" style="left:752px;top:652px">Double Sided Business Card</p>

<section class="sheet card-back">
  <div class="photo" role="img" aria-label="Photograph of an elegant interior with a chandelier"></div>
  <p class="person">Helen Marsh</p>
  <p class="contact"><b>M.</b>07700 900 274<br><b>E.</b> helen@runeestates.co.uk</p>
  <div class="rule"></div>
  <p class="tagline">Giving lasting character to period homes</p>
</section>
</body>
</html>
```